Business Card Design

Velvet Pixel Promotions

An online marketing consulting & strategy business for the cosmetic niche

We specialise in Increasing Leads, Conversions & Content Marketing

I am looking for a very clean, BOLD business card that is simple & effective

Target Market(s)

cosmetic surgeons & cosmetic clinics

Industry/Entity Type

Marketing

Contact Information for Business Card

Darren Okoye
Online Marketing Strategist

Darren@VelvetPixelPromotions.example
0491 268 517

LinkedIn: in/darrenokoye

```html
<!DOCTYPE html>
<html lang="en">
<head>
<meta charset="utf-8">
<title>Velvet Pixel Promotions – Business Card</title>
<link rel="stylesheet" href="https://fonts.googleapis.com/css2?family=Exo+2:wght@600&family=Open+Sans:ital,wght@0,600;0,700;1,700&display=swap">
<style>
  :root {
    --backdrop: #2b3a40;
    --teal: #17a3c4;
    --teal-light: #22b6c6;
    --teal-deep: #0f7f98;
    --blue: #1f9fd8;
    --lime: #a6d12a;
    --green: #3fae3a;
    --green-deep: #2e9a35;
    --paper: #ffffff;
    --ink: #2f3337;
    --ink-soft: #b9bcc0;
    --white: #ffffff;
  }
  * { box-sizing: border-box; margin: 0; padding: 0; }
  html, body {
    width: 1200px; height: 678px; overflow: hidden;
    background: var(--backdrop);
  }
  .canvas {
    position: relative; width: 1200px; height: 678px;
  }
  .card {
    position: absolute; top: 174px;
    width: 540px; height: 330px;
    overflow: hidden; background: var(--paper);
    box-shadow: 0 10px 28px rgba(0,0,0,.35);
  }
  /* ---------- front ---------- */
  .card--front {
    left: 40px;
    background: linear-gradient(160deg, var(--teal) 0%, var(--teal-light) 70%, #2cc0b0 100%);
  }
  .front__ring {
    position: absolute; left: 225px; top: 70px;
    width: 430px; height: 430px; border-radius: 50%;
    background: linear-gradient(200deg, var(--lime) 0%, #5cc24a 60%, var(--green) 100%);
  }
  .front__disc {
    position: absolute; left: 265px; top: 115px;
    width: 380px; height: 380px; border-radius: 50%;
    background: var(--paper);
  }
  .front__name {
    position: absolute; left: 34px; top: 52px;
    font: 700 34px/1 "Open Sans", sans-serif; color: var(--white);
    letter-spacing: -0.3px;
  }
  .front__role {
    position: absolute; left: 36px; top: 90px;
    font: italic 700 13.5px/1 "Open Sans", sans-serif; color: var(--teal-deep);
    letter-spacing: 0.3px;
  }
  .front__web {
    position: absolute; left: 36px; top: 110px;
    font: 600 13px/1 "Open Sans", sans-serif; color: var(--white);
  }
  .contact-list {
    position: absolute; left: 36px; top: 138px;
    list-style: none;
    font: 600 13px/1 "Open Sans", sans-serif; color: var(--white);
  }
  .contact-list li {
    display: flex; align-items: center; gap: 12px; height: 22px;
  }
  .contact-list svg { width: 16px; height: 14px; flex: none; }
  .contact-list .icon-square {
    width: 12px; height: 12px; margin: 0 2px; background: var(--white); flex: none;
  }
  .wordmark {
    position: absolute; left: 330px; top: 208px;
    display: flex; align-items: center; gap: 12px;
  }
  .wordmark__dot {
    width: 38px; height: 38px; border-radius: 50%; background: var(--green); flex: none;
  }
  .wordmark__name {
    font: 600 19px/1.02 "Exo 2", sans-serif; color: var(--ink);
    letter-spacing: 1.6px; text-transform: uppercase;
  }
  /* ---------- back ---------- */
  .card--back { left: 620px; }
  .back__blue {
    position: absolute; left: 0; top: 0; width: 255px; height: 275px;
    background: linear-gradient(135deg, #1b9fd0 0%, var(--teal-light) 100%);
  }
  .back__green {
    position: absolute; right: 0; top: 85px; width: 120px; height: 245px;
    background: linear-gradient(90deg, #6cc23c 0%, var(--green-deep) 100%);
  }
  .back__disc {
    position: absolute; left: 150px; top: 50px;
    width: 210px; height: 210px; border-radius: 50%;
    background: linear-gradient(210deg, var(--lime) 0%, #56be48 100%);
  }
  .back__title {
    position: absolute; right: 18px; top: 26px;
    font: 600 15px/1 "Exo 2", sans-serif; color: var(--ink);
    letter-spacing: 1.8px; text-transform: uppercase;
  }
  .back__echo {
    position: absolute; left: 60px; top: 210px;
    font: 600 13px/1 "Exo 2", sans-serif; color: var(--ink-soft);
    letter-spacing: 2.6px; text-transform: uppercase;
  }
</style>
</head>
<body>
<main class="canvas">

  <section class="card card--front" aria-label="Business card front">
    <div class="front__ring"></div>
    <div class="front__disc"></div>

    <h1 class="front__name">Darren Okoye</h1>
    <p class="front__role">Online Marketing Strategist</p>
    <p class="front__web">VelvetPixelPromotions.example</p>

    <ul class="contact-list">
      <li>
        <svg viewBox="0 0 16 12" aria-hidden="true"><rect x="0.5" y="0.5" width="15" height="11" fill="#fff"/><path d="M0.5 0.5 L8 7 L15.5 0.5" fill="none" stroke="#17a3c4" stroke-width="1.2"/></svg>
        Darren@VelvetPixelPromotions.example
      </li>
      <li><span class="icon-square" aria-hidden="true"></span>in/darrenokoye</li>
      <li>
        <svg viewBox="0 0 16 16" aria-hidden="true"><path d="M3.5 1 L6 1 L7 5 L5.3 6.3 C6.2 8.2 7.8 9.8 9.7 10.7 L11 9 L15 10 L15 12.5 C15 13.9 13.9 15 12.5 15 C6.7 15 1 9.3 1 3.5 C1 2.1 2.1 1 3.5 1 Z" fill="#fff"/></svg>
        0491 268 517
      </li>
    </ul>

    <div class="wordmark">
      <span class="wordmark__dot" aria-hidden="true"></span>
      <span class="wordmark__name">Velvet<br>Pixel<br>Promotions</span>
    </div>
  </section>

  <section class="card card--back" aria-label="Business card back">
    <div class="back__blue"></div>
    <div class="back__green"></div>
    <div class="back__disc" aria-hidden="true"></div>
    <p class="back__title">Velvet Pixel Promotions</p>
    <p class="back__echo">Velvet Pixel Promotions</p>
  </section>

</main>
</body>
</html>
```